Supplement label for Brain health

I need a design for a supplement this supplement is a brain boost supplement.

The Name is Cortiva Plus.

I have attached other labels I like. This is for 50 plus demographic so the lettering needs to be easy to read and stand out. I have attached a dummy label template that once the winner is choosen then they will get the real supplement facts etc.

Clean desgin easy to read.

This file must be finished in AI format.

Target Market(s)

50 plus 70 percent female 30 percent male

Industry/Entity Type

Supplement

Font styles to use
Other font styles liked:
• Myrid pro maybe

Requirements
Must have
• easy to read text so no colors that hide text or hard to read.

```html
<!DOCTYPE html>
<html lang="en">
<head>
<meta charset="utf-8">
<title>Cortiva Plus – Brain Booster Label</title>
<link rel="stylesheet" href="https://fonts.googleapis.com/css2?family=Fira+Sans+Condensed:wght@600;700&family=Fira+Sans+Extra+Condensed:wght@700&family=PT+Sans&display=swap">
<style>
  :root {
    --page-bg: #ececec;
    --label-bg: #ffffff;
    --brand-blue: #0b5aa2;
    --brand-blue-light: #2f86cf;
    --brand-green: #2f8f1f;
    --accent-lime: #7cbd2a;
    --art-deep: #0a6f9a;
    --art-light: #5fd0ea;
    --text-white: #ffffff;
  }
  * { margin: 0; padding: 0; box-sizing: border-box; }
  html, body {
    width: 1200px;
    height: 1200px;
    overflow: hidden;
    background: var(--page-bg);
  }
  .label {
    position: absolute;
    left: 150px;
    top: 88px;
    width: 900px;
    height: 1024px;
    background: var(--label-bg);
    box-shadow: 0 2px 10px rgba(0,0,0,0.08);
  }
  .label-graphics {
    position: absolute;
    inset: 0;
    width: 900px;
    height: 1024px;
  }
  .brand-name {
    font-family: "PT Sans", sans-serif;
    font-size: 54px;
    fill: var(--text-white);
  }
  .headline {
    font-family: "Fira Sans Extra Condensed", sans-serif;
    font-weight: 700;
    font-size: 262px;
  }
  .benefit {
    font-family: "Fira Sans Condensed", sans-serif;
    font-weight: 600;
    font-size: 46px;
    fill: var(--brand-green);
  }
  .supplement-tag {
    font-family: "Fira Sans Condensed", sans-serif;
    font-weight: 700;
    font-size: 43px;
    fill: var(--text-white);
  }
  .brain-art {
    position: absolute;
    left: 115px;
    top: 636px;
    width: 220px;
    height: 250px;
    border-radius: 48% 52% 40% 45%;
    background: radial-gradient(circle at 45% 40%, var(--art-light), var(--art-deep) 75%);
  }
</style>
</head>
<body>
  <main class="label">
    <svg class="label-graphics" viewBox="0 0 900 1024" xmlns="http://www.w3.org/2000/svg">
      <defs>
        <linearGradient id="headlineFill" x1="0" y1="0" x2="0" y2="1">
          <stop offset="0" stop-color="var(--brand-blue-light)"/>
          <stop offset="0.5" stop-color="var(--brand-blue)"/>
          <stop offset="1" stop-color="var(--brand-blue)"/>
        </linearGradient>
      </defs>

      <!-- top brand band -->
      <path class="brand-band" d="M300 0 H900 V100 H390 Q340 100 320 60 Z" fill="var(--brand-blue)"/>
      <circle class="brand-dot" cx="465" cy="50" r="20" fill="var(--text-white)"/>
      <text class="brand-name" x="500" y="70">Cortiva Plus</text>

      <!-- product name -->
      <text class="headline" x="100" y="372" textLength="615" lengthAdjust="spacingAndGlyphs" fill="url(#headlineFill)">BRAIN</text>
      <text class="headline" x="100" y="600" textLength="715" lengthAdjust="spacingAndGlyphs" fill="url(#headlineFill)">BOOSTER</text>

      <!-- benefits -->
      <rect class="benefit-rule" x="456" y="643" width="5" height="251" fill="var(--brand-green)"/>
      <text class="benefit" x="493" y="722">- Promotes Brain</text>
      <text class="benefit" x="518" y="779">function*</text>
      <text class="benefit" x="493" y="844">- 30 Capsules</text>

      <!-- bottom band -->
      <rect class="bottom-rule" x="0" y="894" width="900" height="10" fill="var(--brand-blue)"/>
      <path class="bottom-accent" d="M520 904 H900 V1001 H620 Z" fill="var(--accent-lime)"/>
      <path class="bottom-band" d="M0 904 H520 L620 1001 H0 Z" fill="var(--brand-blue)"/>
      <text class="supplement-tag" x="80" y="970">DIETARY SUPPLEMENT</text>
    </svg>

    <div class="brain-art" role="img" aria-label="Illustration of a glowing blue human brain with neural connections"></div>
  </main>
</body>
</html>
```